Elegant, Playful ReDesign of Paperlark Website in wordpress - Budget has been raised

Project Brief: Paperlark Website Redesign in WordPress

Introduction: Paperlark, a cutting-edge document creation solution, aims to revolutionize the tedious process of crafting contracts, offers, forms, and other documents. By saving customers valuable time, streamlining workflows, and minimizing human error, Paperlark has become an essential tool. As a technology company with a diverse clientele, we're set to boost our online presence through a refreshed WordPress website. Beyond a modernized website, we aspire to establish a stronger brand identity, incorporating graphic elements seamlessly into our online presence.

Current Status: Currently hosted on WordPress, Paperlark's existing website serves its purpose but is ready for a visual transformation. Our goal is to maintain a modern and attractive appearance while upholding our commitment to simplicity and efficiency. Notably, the website is currently only in Danish. The redesigned structure should include a language switch function to cater to future international customers.

Objectives:
• Modern Aesthetic: Redesign the website with a fresh and modern vibe, reflecting innovation in the document creation sphere.
• User-Friendly: Prioritize an intuitive design for seamless navigation, ensuring visitors easily understand our offerings and benefits.
• Informative Content: Strike a balance between attractiveness and informativeness, clearly communicating Paperlark's value proposition and simplifying business processes.
• Graphic Elements: Integrate visually appealing graphics that enhance the site's aesthetics and contribute to our overall visual identity. These elements should be versatile for future use in social media, advertisements, and other branding materials.
• Brand Recognition: Maintain our current logo and color scheme while exploring creative ways to establish a distinctive brand identity. The website should be a cornerstone for a cohesive branding strategy.
• Media Integration: Include images or videos on the website to enhance engagement. Find suitable, free-to-use visuals.
• Responsiveness: Ensure the design is responsive and works seamlessly on all devices.
• Demo Booking Form: Improve the design of the form to book a demo.
• Multilingual Support: Enable language transformation; the website is currently in Danish but should cater to other countries.

Guidelines:
• Typography: Up to the designer's discretion.
• Images/Videos: Must be free to use without additional charges.
• WordPress Theme: Use any WordPress theme below $100.
• Logo Redesign: Not needed; stick to the referenced color palette, as our new logo uses these colors.
• Color Palette: Stick to the existing company colors for consistency:
RGB
• #000b3c
• #004c6c
• #319ac3
• Greytones and white are also allowed
• Creativity Encouraged: Embrace creativity within the color palette for the layout, visuals, and overall user experience.

Conclusion: The Paperlark website redesign marks an exciting opportunity to enhance our online presence. Our goal is to achieve a balance between a modern, attractive design and a clear, informative representation of our innovative solutions. We envision the revamped website as the foundation for a compelling online brand presence, with versatile graphic elements resonating across various digital platforms.

Sections that the website must include: Space for customer logos, space for testimonials, Space and redesign for display of price structure and price comparison, sections for company details and other information.

Design should also include a redesign of the customer cases section.
Generally there should just be a redesign of all things that are on the website.

Link to current website: https://paperlark-example.com/

+50 employees.

Document automation

Coded - Design and coding required

5+ page

0054AA
0677BA
7BADD7
CADEEF
E8F1F8

• The new webpage must have the same pages as the current one. Frontpage, Book demo, About us, Case stories and Pricing

```html
<!DOCTYPE html>
<html lang="en">
<head>
<meta charset="utf-8">
<title>Paperlark – Prices</title>
<link rel="stylesheet" href="https://fonts.googleapis.com/css2?family=Teko:wght@500;600&family=Roboto:wght@300;400;500;700&family=Lato:wght@400;700&family=Montserrat:wght@600;700&display=swap">
<style>
:root{
  --navy:#002440;
  --teal:#006d8f;
  --teal-dark:#004c6c;
  --cyan:#00a3dd;
  --brand-blue:#1aa0d8;
  --row-grey:#e7e7e7;
  --muted:#a9a9a9;
  --ink:#1c1c1c;
  --band:#c8e0e5;
  --faq-bg:#f4f4f4;
  --line:#d4d4d4;
}
*{margin:0;padding:0;box-sizing:border-box}
html,body{width:1200px;height:2598px;overflow:hidden;background:#fff}
body{position:relative;font-family:"Roboto",sans-serif;color:var(--ink)}
.abs{position:absolute}

/* header */
.brand{left:88px;top:24px;display:flex;align-items:center;gap:10px}
.brand-mark{width:40px;height:46px;background:var(--brand-blue)}
.brand-name{font:700 28px "Roboto",sans-serif;color:var(--brand-blue);letter-spacing:-.3px}
.nav{left:590px;top:44px;display:flex;align-items:center;font:500 12.5px "Roboto",sans-serif;color:#111}
.nav a{color:inherit;text-decoration:none;padding:3px 8px;line-height:16px}
.nav .active{border:1px solid var(--teal);margin-right:0}
.nav .login{background:var(--cyan);color:#fff;padding:4px 14px;margin:0 8px 0 8px}

/* intro */
.page-title{left:0;width:1180px;top:128px;text-align:center;font:600 46px/1 "Teko",sans-serif;color:var(--teal-dark);letter-spacing:.5px}
.title-rule{left:492px;top:177px;width:194px;height:3px;background:linear-gradient(90deg,var(--cyan),var(--teal-dark))}
.intro{left:180px;width:820px;top:196px;text-align:center;font:400 14px/19px "Roboto",sans-serif}
.billing{left:426px;top:258px;display:flex;height:35px;font:500 15.5px/35px "Roboto",sans-serif}
.billing span{padding:0 20px}
.billing .off{background:#d3d3d3;color:#8e8e8e;width:176px;text-align:center}
.billing .on{background:var(--teal);color:#fff;width:177px;text-align:center}

/* plans */
.plan{background:#fff;border-radius:8px;box-shadow:0 2px 8px rgba(0,0,0,.28);overflow:hidden}
.plan-head{position:absolute;left:0;top:0;width:100%;text-align:center;color:#fff}
.plan-name{position:absolute;left:0;width:100%;font:600 46px/1 "Teko",sans-serif;letter-spacing:.5px}
.plan-quota{position:absolute;left:0;width:100%;font:300 13.5px "Roboto",sans-serif}
.plan-price{position:absolute;background:#fff;border-radius:30px;box-shadow:0 3px 6px rgba(0,0,0,.2);display:flex;align-items:center;justify-content:center;gap:6px;font-family:"Teko",sans-serif;color:#3a3a3a}
.plan-price b{font-weight:500;font-size:31px;line-height:1;padding-top:4px}
.plan-price small{font-weight:500;font-size:20px;color:#7a7a7a;padding-top:6px}
.features{position:absolute;left:0;width:100%;list-style:none}
.features li{text-align:center;font:400 15.5px "Roboto",sans-serif;color:var(--ink);display:flex;align-items:center;justify-content:center}
.features li:nth-child(odd){background:var(--row-grey)}
.features li.off{color:var(--muted)}
.btn{position:absolute;background:var(--teal);color:#fff;font:400 18px "Roboto",sans-serif;display:flex;align-items:center;justify-content:center;letter-spacing:.3px;text-decoration:none}

.plan-side{width:314px;height:743px;top:355px}
.plan-side .plan-head{height:133px;background:var(--cyan)}
.plan-side .plan-name{top:20px}
.plan-side .plan-quota{top:62px}
.plan-side .plan-price{left:34px;top:104px;width:246px;height:53px}
.plan-side .features{top:175px}
.plan-side .features li{height:30.4px}
.plan-side .btn{left:82px;top:687px;width:162px;height:38px}

.plan-pro{left:432px;top:315px;width:348px;height:823px}
.plan-pro .plan-head{height:147px;background:var(--teal)}
.plan-pro .plan-name{top:20px;font-size:56px}
.plan-pro .plan-quota{top:69px;font-size:14.5px}
.plan-pro .plan-price{left:38px;top:115px;width:272px;height:58px}
.plan-pro .plan-price b{font-size:33px}
.plan-pro .features{top:193px}
.plan-pro .features li{height:33.7px;font-size:17.5px}
.plan-pro .btn{left:90px;top:760px;width:179px;height:42px;font-size:20px}

/* enterprise */
.enterprise{left:0;top:1247px;width:1200px;height:365px;background:var(--band);border-top-left-radius:200px 190px;text-align:center}
.enterprise h2{font:500 22px "Roboto",sans-serif;color:#111;position:absolute;left:0;width:1188px}
.enterprise p{font:400 14px/15px "Roboto",sans-serif;position:absolute;left:190px;width:808px}
.enterprise .btn{left:522px;top:296px;width:179px;height:38px;font-size:18.5px}

/* faq */
.faq-title{left:104px;top:1642px;font:500 21.5px "Roboto",sans-serif;color:#111}
.faq{left:81px;top:1682px;width:1011px;height:476px;background:var(--faq-bg)}
.faq-item{position:absolute;left:14px;width:983px;background:#fff;border:1px solid var(--line)}
.faq-q{display:flex;align-items:center;height:38px;font:400 12.8px "Lato",sans-serif;color:#222;padding-left:10px}
.faq-q svg{margin-right:10px;flex:none}
.faq-a{border-top:1px solid var(--line);padding:22px 28px 0 29px;font:400 12.8px/21px "Lato",sans-serif;color:#222;height:84px}

/* footer */
.footer{left:0;top:2188px;width:1200px;height:410px;background:var(--navy);color:#fff}
.footer-brand{position:absolute;left:85px;top:36px;width:253px;height:70px;background:#fff;display:flex;align-items:center;justify-content:center;gap:10px}
.footer-brand .brand-mark{width:34px;height:40px}
.footer-contact{position:absolute;left:86px;top:127px;font:400 16px/24px "Roboto",sans-serif}
.follow{position:absolute;left:82px;top:206px;font:700 13px "Roboto",sans-serif}
.socials{position:absolute;left:82px;top:231px;display:flex;gap:14px}
.socials span{width:24px;height:24px;border:2px solid #fff;border-radius:50%}
.footer-nav{position:absolute;left:491px;top:127px;list-style:none;font:700 13.5px/26px "Montserrat",sans-serif;letter-spacing:.8px}
.meet{position:absolute;left:776px;top:126px;font:400 16px/24px "Roboto",sans-serif}
.meet h3{font:700 19px/27px "Roboto",sans-serif}
.footer-rule{position:absolute;left:115px;top:315px;width:974px;height:1px;background:#4d5f73}
.copyright{position:absolute;left:0;width:1160px;top:343px;text-align:center;font:400 10px "Roboto",sans-serif;color:#aab3be}
</style>
</head>
<body>

<header>
  <div class="abs brand"><span class="brand-mark"></span><span class="brand-name">Paperlark</span></div>
  <nav class="abs nav">
    <a href="https://paperlark-example.com/">Home</a>
    <a>Customer Cases</a>
    <a>Video</a>
    <a>Live Demo</a>
    <a class="active">Prices</a>
    <a>About Us</a>
    <a class="login">Login</a>
    <a>English</a>
  </nav>
</header>

<h1 class="abs page-title">PRICES</h1>
<div class="abs title-rule"></div>
<p class="abs intro">Choose between three different standard models in relation to which contracts you want automated. Contact us if you have more than five contracts, and we will tailor an Enterprise model that is adapted to your needs.</p>
<div class="abs billing"><span class="off">Monthly Payment</span><span class="on">Annually Payment</span></div>

<section class="abs plan plan-side" style="left:94px">
  <div class="plan-head"><div class="plan-name">STARTER</div><div class="plan-quota">250 documents / Year</div></div>
  <div class="plan-price"><b>DDK 795</b><small>Per Month</small></div>
  <ul class="features">
    <li>1 contract templates</li><li>1 user</li><li>+ DKK 95 per additional user</li><li>Export to Word</li><li>Export to Pdf</li><li>Own design</li>
    <li class="off">Digital signature</li><li class="off">Reviewproces</li><li class="off">More languages</li><li class="off">Product listing</li><li class="off">Employee posting</li><li class="off">Documents in mail</li><li class="off">Integration to CRM</li><li class="off">Customer/client request</li><li class="off">Raw data in Excel</li><li class="off">API access</li>
  </ul>
  <a class="btn">BOOK DEMO</a>
</section>

<section class="abs plan plan-pro">
  <div class="plan-head"><div class="plan-name">PRO</div><div class="plan-quota">1000 documents / Year</div></div>
  <div class="plan-price"><b>DDK 1,595</b><small>Per Month</small></div>
  <ul class="features">
    <li>2 contract templates</li><li>1 user</li><li>+ DKK 95 per additional user</li><li>Export to Word</li><li>Export to Pdf</li><li>Own design</li>
    <li>Digital signature</li><li>Reviewproces</li><li>More languages</li><li>Product listing</li><li>Employee posting</li><li>Documents in mail</li><li>Integration to CRM</li><li class="off">Customer/client request</li><li class="off">Raw data in Excel</li><li class="off">API access</li>
  </ul>
  <a class="btn">BOOK DEMO</a>
</section>

<section class="abs plan plan-side" style="left:805px">
  <div class="plan-head"><div class="plan-name">BUSINESS</div><div class="plan-quota">2000 documents / Year</div></div>
  <div class="plan-price"><b>DDK 2795</b><small>Per Month</small></div>
  <ul class="features">
    <li>4 contract templates</li><li>1 user</li><li>+ DKK 95 per additional user</li><li>Export to Word</li><li>Export to Pdf</li><li>Own design</li>
    <li>Digital signature</li><li>Reviewproces</li><li>More languages</li><li>Product listing</li><li>Employee posting</li><li>Documents in mail</li><li>Integration to CRM</li><li>Customer/client request</li><li>Raw data in Excel</li><li>API access</li>
  </ul>
  <a class="btn">BOOK DEMO</a>
</section>

<section class="abs enterprise">
  <h2 style="top:22px">Enterprise model</h2>
  <p style="top:60px">We can tailor a model adapted to your business with unliited use.</p>
  <h2 style="top:108px">Number of templates and users</h2>
  <p style="top:145px">If you have many contracts, we tailor a model for you. We can automate as many offers, contracts and other documents as you need, just as we can give access to all the users you want.</p>
  <h2 style="top:208px">Continuous update</h2>
  <p style="top:245px">We can also offer continuous updating of your automated documents if you do not want to make the updates yourself.</p>
  <a class="btn">BOOK DEMO</a>
</section>

<h2 class="abs faq-title">FAQ for subscriptions</h2>
<section class="abs faq">
  <div class="faq-item" style="top:12px">
    <div class="faq-q"><svg width="14" height="14" viewBox="0 0 14 14"><rect x=".5" y=".5" width="13" height="13" fill="none" stroke="#aaa"/><path d="M3 7h8" stroke="#888"/></svg>Can I update an automated contract myself?</div>
    <div class="faq-a">Customize your offers, contracts or other documents yourself in our Designer. After your template has been automated, you get full access. We can also help you with updates, so you don't have to worry about the technology in the engine room. Contact us if you want help with updates.</div>
  </div>
  <div class="faq-item" style="top:140px"><div class="faq-q"><svg width="14" height="14" viewBox="0 0 14 14"><rect x=".5" y=".5" width="13" height="13" fill="none" stroke="#aaa"/><path d="M3 7h8M7 3v8" stroke="#888"/></svg>Can I use a digital signature?</div></div>
  <div class="faq-item" style="top:179px"><div class="faq-q"><svg width="14" height="14" viewBox="0 0 14 14"><rect x=".5" y=".5" width="13" height="13" fill="none" stroke="#aaa"/><path d="M3 7h8M7 3v8" stroke="#888"/></svg>How many documents can I create?</div></div>
  <div class="faq-item" style="top:217px"><div class="faq-q"><svg width="14" height="14" viewBox="0 0 14 14"><rect x=".5" y=".5" width="13" height="13" fill="none" stroke="#aaa"/><path d="M3 7h8M7 3v8" stroke="#888"/></svg>What is a customer/client request?</div></div>
  <div class="faq-item" style="top:256px"><div class="faq-q"><svg width="14" height="14" viewBox="0 0 14 14"><rect x=".5" y=".5" width="13" height="13" fill="none" stroke="#aaa"/><path d="M3 7h8M7 3v8" stroke="#888"/></svg>Can I make my contract template smaller?</div></div>
  <div class="faq-item" style="top:294px"><div class="faq-q"><svg width="14" height="14" viewBox="0 0 14 14"><rect x=".5" y=".5" width="13" height="13" fill="none" stroke="#aaa"/><path d="M3 7h8M7 3v8" stroke="#888"/></svg>Can I get more space for my documents?</div></div>
  <div class="faq-item" style="top:333px"><div class="faq-q"><svg width="14" height="14" viewBox="0 0 14 14"><rect x=".5" y=".5" width="13" height="13" fill="none" stroke="#aaa"/><path d="M3 7h8M7 3v8" stroke="#888"/></svg>When will my subscription be activated?</div></div>
  <div class="faq-item" style="top:371px"><div class="faq-q"><svg width="14" height="14" viewBox="0 0 14 14"><rect x=".5" y=".5" width="13" height="13" fill="none" stroke="#aaa"/><path d="M3 7h8M7 3v8" stroke="#888"/></svg>Can I change my subscription or cancel whenever I want?</div></div>
  <div class="faq-item" style="top:410px"><div class="faq-q"><svg width="14" height="14" viewBox="0 0 14 14"><rect x=".5" y=".5" width="13" height="13" fill="none" stroke="#aaa"/><path d="M3 7h8M7 3v8" stroke="#888"/></svg>What is an automated contract?</div></div>
</section>

<footer class="abs footer">
  <div class="footer-brand"><span class="brand-mark"></span><span class="brand-name">Paperlark</span></div>
  <div class="footer-contact">Mail: contact@paperlark-example.com<br>Phone: +45 70 11 22 33<br>Address: Skrivervej 14, 2750 Ballerup</div>
  <div class="follow">Follow us on</div>
  <div class="socials" aria-label="Social links"><span></span><span></span><span></span><span></span></div>
  <ul class="footer-nav"><li>HOME</li><li>CUSTOMER REVIEW</li><li>VIDEO DEMO</li><li>PRICES</li><li>ABOUT US</li></ul>
  <div class="meet"><h3>Meet Us Online</h3>We Would Love To Link And Share<br>Thoughts And Ideas. Follow Us And Stay<br>Updated On The Latest News.</div>
  <div class="footer-rule"></div>
  <div class="copyright">Copyright © 2024 Paperlark, All rights reserved.</div>
</footer>

</body>
</html>
```